Brambleway Gardening Services. A6 flyer single sided

Need an A6 flyer designing. Single sided.
I am a gardener.
I do lawn mowing - one-off garden tidy ups or regular fortnightly visits.
All kinds of trees expertly felled, topped or pruned.
Hedge cutting.
Fencing replaced or repaired.
Fully insured.
Access to fully qualified and licenced tree arborist
07741 206319 or 01632 470918.

I have attached my business card and letter head logo.
I'm open to new designs without incorporating any of my artwork.

Industry/Entity Type

Gardener

```html
<!DOCTYPE html>
<html lang="en">
<head>
<meta charset="utf-8">
<title>Brambleway Gardening Services – A6 Flyer</title>
<link rel="stylesheet" href="https://fonts.googleapis.com/css2?family=Poppins:ital,wght@0,500;0,600;0,700;0,800;1,500&display=swap">
<style>
  :root {
    --page: #ecebe6;
    --green-deep: #1f4d12;
    --green-mid: #2f6a1a;
    --green-bright: #4f8d24;
    --lime: #c7d932;
    --lime-soft: #dce96a;
    --white: #ffffff;
    --ink-green: #1c3f0c;
  }
  * { margin: 0; padding: 0; box-sizing: border-box; }
  html, body { width: 1200px; height: 1000px; overflow: hidden; }
  body { background: var(--page); font-family: "Poppins", sans-serif; }

  .flyer {
    position: absolute; left: 280px; top: 50px;
    width: 640px; height: 900px; overflow: hidden;
    background: linear-gradient(160deg, var(--green-bright) 0%, var(--green-mid) 45%, var(--green-deep) 100%);
    box-shadow: 0 6px 24px rgba(0,0,0,.18);
  }
  .flyer-art { position: absolute; inset: 0; }

  .brand { position: absolute; left: 48px; top: 440px; width: 560px; }
  .brand-name {
    font-size: 64px; font-weight: 800; color: var(--white);
    letter-spacing: -1px; line-height: 1;
  }
  .brand-tag {
    margin-top: 6px; font-size: 20px; font-weight: 500; color: var(--lime);
    letter-spacing: 10px; text-transform: lowercase;
  }
  .rule { position: absolute; left: 48px; width: 544px; height: 3px; background: var(--lime); }
  .rule-top { top: 560px; }
  .rule-bottom { top: 614px; }
  .visits {
    position: absolute; left: 48px; top: 572px; width: 544px;
    font-size: 19px; font-style: italic; font-weight: 500; color: var(--white);
    white-space: nowrap;
  }
  .services { position: absolute; left: 48px; top: 628px; width: 560px; }
  .services-main { font-size: 25px; font-weight: 700; color: var(--lime); line-height: 1.4; }
  .services-extra { font-size: 18px; font-weight: 600; color: var(--white); line-height: 1.3; }

  .contact-band {
    position: absolute; left: 0; top: 762px; width: 640px; height: 66px;
    background: linear-gradient(90deg, var(--lime-soft), var(--lime));
    display: flex; align-items: center; gap: 34px; padding: 0 34px;
    color: var(--ink-green); font-weight: 700;
  }
  .contact-name { font-size: 20px; }
  .contact-phone { font-size: 24px; }
  .contact-email {
    position: absolute; left: 64px; top: 846px;
    font-size: 20px; font-weight: 500; color: var(--white);
  }
</style>
</head>
<body>
  <main class="flyer">
    <svg class="flyer-art" width="640" height="900" viewBox="0 0 640 900">
      <defs>
        <linearGradient id="gardenPhoto" x1="0" y1="0" x2="1" y2="1">
          <stop offset="0" stop-color="#b9dc6a"/>
          <stop offset="0.45" stop-color="#8fbf45"/>
          <stop offset="0.75" stop-color="#a9855a"/>
          <stop offset="1" stop-color="#8a6440"/>
        </linearGradient>
      </defs>
      <path class="swoosh-lime" d="M0,300 C220,330 420,420 640,440 V472 C420,460 220,390 0,360 Z" fill="var(--lime)"/>
      <path class="swoosh-white" d="M0,262 C220,300 420,400 640,420 V452 C420,440 220,360 0,320 Z" fill="var(--white)"/>
      <path class="garden-photo" role="img"
            aria-label="Photo of garden tools – watering can, gloves, rake, wellington boots and trowel – on a wooden deck against green grass"
            d="M0,0 H640 V420 C420,400 220,300 0,262 Z" fill="url(#gardenPhoto)"/>
    </svg>

    <header class="brand">
      <h1 class="brand-name">Brambleway</h1>
      <p class="brand-tag">gardening services</p>
    </header>

    <div class="rule rule-top"></div>
    <p class="visits">Regular Fortnightly Visits or One-Off Garden Tidy-Ups</p>
    <div class="rule rule-bottom"></div>

    <section class="services">
      <p class="services-main">Lawn Mowing &amp; Hedge Cutting</p>
      <p class="services-extra">All Trees Expertly Felled, Topped or Pruned<br>Fencing Replaced or Repaired<br>Fully Insured · Licenced Tree Arborist Access</p>
    </section>

    <footer>
      <div class="contact-band">
        <span class="contact-name">Sam Hartley</span>
        <span class="contact-phone">07741 206319</span>
        <span class="contact-phone">01632 470918</span>
      </div>
      <p class="contact-email">brambleway@leafpost.com</p>
    </footer>
  </main>
</body>
</html>
```